(Expedite) Business Card
Pacific Motor Keep
(Expedite) Business Card - Real Estate
Creative Brief
Use standard fonts
please be creative - ok to use a different font than the logo
Professional
State-of-the-Art Car Storage & Collection Management
27405 W. Lindenmoor Avenue Marlow Bay, CA 93071
info@pacificmotorkeep.com
www.pacificmotorkeep.com
Logo on front of business card, contact information on back of business card.
Contact information on back of business card.
PacificMotorKeep PacificMotorKeep

```html
<!DOCTYPE html>
<html lang="en">
<head>
<meta charset="utf-8">
<title>Pacific Motor Keep – Business Card</title>
<link rel="stylesheet" href="https://fonts.googleapis.com/css2?family=Montserrat:wght@400;600;800&display=swap">
<style>
  :root {
    --stage: #8a8a8a;
    --ink: #111111;
    --paper: #ffffff;
    --orange: #f07a1e;
    --text-dark: #2a2a2a;
  }
  * { margin: 0; padding: 0; box-sizing: border-box; }
  html, body { width: 1200px; height: 908px; overflow: hidden; }
  body {
    background: var(--stage);
    font-family: "Montserrat", Arial, sans-serif;
    position: relative;
  }
  .card {
    position: absolute;
    width: 520px;
    height: 300px;
    border-radius: 18px;
    overflow: hidden;
  }
  /* Front */
  .card-front {
    left: 60px; top: 180px;
    background: var(--ink);
    color: var(--paper);
  }
  .card-front .wordmark {
    position: absolute;
    left: 40px; top: 88px;
    display: flex; align-items: center; gap: 14px;
  }
  .wordmark .mark-square {
    width: 18px; height: 18px;
    background: var(--orange);
    flex: none;
  }
  .card-front .brand-name {
    font-weight: 800;
    font-size: 30px;
    letter-spacing: 1px;
    text-transform: uppercase;
    line-height: 1.1;
  }
  .card-front .tagline {
    position: absolute;
    left: 40px; top: 176px;
    color: var(--orange);
    font-size: 12.5px;
    font-weight: 600;
  }
  /* Back */
  .card-back {
    left: 620px; top: 410px;
    background: var(--paper);
    color: var(--text-dark);
  }
  .card-back .edge-band {
    position: absolute; left: 0; top: 0; bottom: 0;
    width: 22px; background: var(--ink);
  }
  .card-back .rule {
    position: absolute; left: 22px; right: 0; top: 138px;
    height: 4px; background: var(--orange);
  }
  .card-back .wordmark {
    position: absolute; left: 46px; top: 100px;
  }
  .card-back .brand-name {
    font-weight: 800; font-size: 20px;
    text-transform: uppercase; color: var(--ink);
    letter-spacing: .5px;
  }
  .card-back .person {
    position: absolute; left: 46px; top: 158px;
  }
  .person .name { color: var(--orange); font-weight: 600; font-size: 17px; }
  .person .role { color: var(--text-dark); font-weight: 600; font-size: 12px; margin-top: 2px; }
  .card-back .contact {
    position: absolute; left: 220px; top: 158px;
    list-style: none; font-size: 11px; line-height: 1.6;
  }
  .contact .address { margin-bottom: 4px; }
  .contact li { display: flex; align-items: center; gap: 6px; }
  .contact svg { width: 13px; height: 13px; flex: none; }
</style>
</head>
<body>

<section class="card card-front" aria-label="Business card front">
  <div class="wordmark">
    <span class="mark-square"></span>
    <span class="brand-name">Pacific<br>Motor Keep</span>
  </div>
  <p class="tagline">State-of-the-Art Car Storage &amp; Collection Management</p>
</section>

<section class="card card-back" aria-label="Business card back">
  <div class="edge-band"></div>
  <div class="rule"></div>
  <div class="wordmark"><span class="brand-name">Pacific Motor Keep</span></div>
  <div class="person">
    <p class="name">Your Name</p>
    <p class="role">Position</p>
  </div>
  <ul class="contact">
    <li class="address">27405 W. Lindenmoor Avenue<br>Marlow Bay, CA 93071</li>
    <li><svg viewBox="0 0 14 14"><circle cx="7" cy="7" r="7" fill="#f07a1e"/><path d="M4.5 3.5l1.5 0 .6 2-1 .7a5 5 0 0 0 2.2 2.2l.7-1 2 .6v1.5c0 .5-.4.8-.9.8A6 6 0 0 1 3.7 4.4c0-.5.3-.9.8-.9z" fill="#fff"/></svg>(555) 014-8820</li>
    <li><svg viewBox="0 0 14 14"><circle cx="7" cy="7" r="7" fill="#f07a1e"/><rect x="4" y="4" width="6" height="6" rx="1" fill="#fff"/></svg>(555) 019-2264</li>
    <li><svg viewBox="0 0 14 14"><circle cx="7" cy="7" r="7" fill="#f07a1e"/><rect x="3.5" y="4.5" width="7" height="5" fill="#fff"/><path d="M3.5 4.5L7 7.3l3.5-2.8" stroke="#f07a1e" stroke-width=".8" fill="none"/></svg>info@pacificmotorkeep.com</li>
    <li><svg viewBox="0 0 14 14"><circle cx="7" cy="7" r="7" fill="#f07a1e"/><circle cx="7" cy="7" r="3.5" fill="none" stroke="#fff" stroke-width="1"/><path d="M3.5 7h7M7 3.5v7" stroke="#fff" stroke-width=".8"/></svg>www.pacificmotorkeep.com</li>
  </ul>
</section>

</body>
</html>
```